The amber lantern with an elephant incorporated in the background

Target Market(s)

Real estate

Industry/Entity Type

Real Estate

Contact Information for Business Card

On back on want my name & number
In front I want the business name, "the amber lantern", below to say staging & design

Logo Text

The amber lantern

Font styles to use
Serif

Colors
000000

Requirements
Must have
• I want an elephant behind the writing in gold transperant

```html
<!DOCTYPE html>
<html lang="en">
<head>
<meta charset="utf-8">
<title>The Amber Lantern – Business Cards</title>
<link rel="stylesheet" href="https://fonts.googleapis.com/css2?family=Michroma&family=Montserrat:wght@400;500&display=swap">
<style>
  :root {
    --page: #ecebea;
    --card: #ffffff;
    --ink: #111111;
    --ink-soft: #7a7a7a;
    --frame: #2a2a2a;
    --gold-1: rgba(224, 205, 160, 0.55);
    --gold-2: rgba(205, 182, 130, 0.35);
    --blush-1: rgba(236, 190, 196, 0.75);
    --blush-2: rgba(244, 214, 218, 0.0);
    --shadow: 0 10px 30px rgba(0, 0, 0, 0.12);
  }
  * { box-sizing: border-box; margin: 0; padding: 0; }
  html, body {
    width: 1200px;
    height: 800px;
    overflow: hidden;
    background: var(--page);
  }
  .sheet {
    width: 1200px;
    height: 800px;
    display: flex;
    align-items: center;
    justify-content: center;
    gap: 40px;
  }
  .card {
    position: relative;
    width: 540px;
    height: 309px;
    background: var(--card);
    box-shadow: var(--shadow);
    overflow: hidden;
  }

  /* Front */
  .card-front .elephant-art {
    position: absolute;
    left: 140px;
    top: 18px;
    width: 330px;
    height: 270px;
    border-radius: 42% 48% 40% 44%;
    background: radial-gradient(ellipse at 45% 50%, var(--gold-1), var(--gold-2) 55%, rgba(255,255,255,0) 75%);
  }
  .brand {
    position: absolute;
    left: 90px;
    top: 128px;
    width: 380px;
  }
  .brand-row {
    display: flex;
    align-items: center;
    gap: 12px;
  }
  .brand-mark {
    width: 10px;
    height: 10px;
    background: var(--ink);
    flex: none;
  }
  .brand-name {
    font-family: "Michroma", sans-serif;
    font-weight: 400;
    font-size: 19px;
    letter-spacing: 0.04em;
    color: var(--ink);
    white-space: nowrap;
  }
  .brand-tagline {
    display: block;
    margin-top: 12px;
    padding-left: 22px;
    font-family: "Montserrat", sans-serif;
    font-weight: 500;
    font-size: 11px;
    letter-spacing: 0.12em;
    color: var(--ink);
  }

  /* Back */
  .card-back .splash-art {
    position: absolute;
    left: 150px;
    top: 72px;
    width: 170px;
    height: 120px;
    border-radius: 50%;
    background: radial-gradient(ellipse at 50% 50%, var(--blush-1), var(--blush-2) 70%);
  }
  .person-name {
    position: absolute;
    left: 190px;
    top: 110px;
    border: 1.5px solid var(--frame);
    padding: 12px 20px 10px;
    font-family: "Michroma", sans-serif;
    font-weight: 400;
    font-size: 20px;
    letter-spacing: 0.18em;
    text-transform: uppercase;
    white-space: nowrap;
  }
  .person-first { color: var(--ink); }
  .person-last { color: var(--ink-soft); }
  .person-phone {
    position: absolute;
    left: 150px;
    top: 214px;
    font-family: "Montserrat", sans-serif;
    font-weight: 500;
    font-size: 12px;
    letter-spacing: 0.22em;
    color: var(--ink);
  }
</style>
</head>
<body>
  <main class="sheet">
    <section class="card card-front">
      <div class="elephant-art" role="img" aria-label="Translucent gold elephant figure behind the business name"></div>
      <div class="brand">
        <div class="brand-row">
          <span class="brand-mark" aria-hidden="true"></span>
          <span class="brand-name">The Amber Lantern</span>
        </div>
        <span class="brand-tagline">Staging &amp; Design</span>
      </div>
    </section>

    <section class="card card-back">
      <div class="splash-art" role="img" aria-label="Soft blush paint splash behind the name"></div>
      <h1 class="person-name"><span class="person-first">Marcus</span> <span class="person-last">Hale</span></h1>
      <p class="person-phone">054-310-7726</p>
    </section>
  </main>
</body>
</html>
```